Web Design Project

Psychotherapist in Private Practice
Practice name "The Steady Harbor"
The population is professional adults seeking life coaching and change consultation
I am including a photo for inspiration ONLY - It includes the theme of light and tree branches. There does not HAVE to be a photograph . An illustration , concept or theme of nature /light / generativity / growth / creativity is acceptable
Clean sharp lines Light colors, minimalist , modern.
There is a separate project for a logo design that will become part of the web design
Here are examples of two logos/websites I like
http://www.quietrivergroup.example/
http://www.brightknollpartners.example/

Target Market(s)

Professional adults seeking life coaching

Industry/Entity Type

Life Coaching

Requirements
Should not have
• Although the business name has 'compassion' in it, designs with hearts in it would have to be pretty stylish, subtle, mature and sophisticated to be considered.

```html
<!DOCTYPE html>
<html lang="en">
<head>
<meta charset="utf-8">
<title>The Steady Harbor</title>
<link rel="stylesheet" href="https://fonts.googleapis.com/css2?family=Mulish:wght@300;400;600;700&display=swap">
<style>
  :root {
    --sand: #d8c6ab;
    --sand-light: #e3d4bd;
    --sand-dark: #cbb797;
    --paper: #f8f6f1;
    --blue: #3fb1e3;
    --blue-light: #6bcdf3;
    --green: #a8d04a;
    --text: #555049;
    --text-dark: #4a4640;
    --rule: #e3dfd6;
    --white: #ffffff;
  }
  * { margin: 0; padding: 0; box-sizing: border-box; }
  html, body { width: 1000px; height: 1200px; overflow: hidden; }
  body {
    position: relative;
    font-family: "Mulish", sans-serif;
    background: var(--paper);
    color: var(--text);
  }
  .header-band {
    position: absolute; left: 0; top: 0; width: 1000px; height: 398px;
    background: linear-gradient(160deg, var(--sand-light) 0%, var(--sand) 45%, var(--sand-dark) 100%);
    border-top: 7px solid #efe8de;
  }
  .accent-rule {
    position: absolute; left: 0; top: 396px; width: 1000px; height: 6px;
    background: var(--green);
    border-top: 2px solid #8c8067;
    box-shadow: 0 2px 3px rgba(0,0,0,0.12);
  }
  .brand { position: absolute; left: 104px; top: 19px; display: flex; align-items: center; }
  .brand-mark { width: 48px; height: 48px; border-radius: 50%; background: var(--white); }
  .brand-name {
    margin-left: 10px; font-size: 15.5px; font-weight: 700; color: var(--text);
    text-transform: uppercase; letter-spacing: 0.2px;
  }
  .main-nav { position: absolute; top: 34px; left: 468px; display: flex; }
  .main-nav a, .footer-nav a {
    font-size: 12.5px; font-weight: 400; color: var(--blue); text-decoration: none;
  }
  .main-nav a { position: absolute; white-space: nowrap; }
  .main-nav a.current, .footer-nav a.current { color: var(--text); }
  .hero-frame {
    position: absolute; left: 103px; top: 82px; width: 794px; height: 292px;
    background: #f7f5f1; box-shadow: 0 1px 3px rgba(0,0,0,0.15);
  }
  .hero-image {
    position: absolute; left: 10px; top: 11px; width: 774px; height: 270px;
    background: linear-gradient(180deg, #2a6fd0 0%, #7bb4ea 40%, #dcefff 52%, #2fb7b0 62%, #6fd7c7 78%, #e8f4f4 100%);
  }
  .hero-panel {
    position: absolute; left: 480px; top: 23px; width: 280px; height: 227px;
    background: rgba(70, 82, 96, 0.72); text-align: center; color: var(--white);
  }
  .hero-title { margin-top: 9px; font-size: 27px; font-weight: 300; line-height: 36px; }
  .hero-title .hl { color: var(--blue-light); }
  .hero-text { margin-top: 8px; font-size: 11px; font-weight: 700; line-height: 17px; padding: 0 10px; }
  .btn {
    display: block; background: var(--blue-light); color: var(--white);
    font-size: 12.5px; font-weight: 600; text-transform: uppercase; text-align: center;
    text-decoration: none; border-bottom: 1px solid #3b9cc6; border-right: 1px solid #3b9cc6;
  }
  .hero-panel .btn { position: absolute; left: 68px; top: 175px; width: 142px; height: 35px; line-height: 35px; }
  .section-title {
    position: absolute; left: 125px; font-size: 16px; font-weight: 600; color: var(--blue);
  }
  .section-rule { position: absolute; left: 103px; width: 795px; height: 1px; background: var(--rule); }
  .intro {
    position: absolute; left: 126px; top: 462px; width: 760px;
    font-size: 13.4px; font-weight: 300; line-height: 29px; color: var(--text);
  }
  .intro .more {
    margin-left: 6px; font-size: 11.5px; font-weight: 700; color: var(--blue);
    text-decoration: none; text-transform: uppercase; letter-spacing: 0.5px;
  }
  .feature-list { position: absolute; top: 688px; list-style: none; }
  .feature-list li {
    height: 33.3px; font-size: 11.6px; font-weight: 700; color: var(--text-dark);
    letter-spacing: 0.3px; display: flex; align-items: flex-start;
  }
  .feature-list svg { margin-right: 11px; margin-top: 2px; flex: none; }
  .gallery-card {
    position: absolute; top: 849px; width: 250px; height: 208px;
    background: var(--white); box-shadow: 0 0 3px rgba(0,0,0,0.15);
  }
  .gallery-card .photo { position: absolute; left: 5px; top: 5px; width: 240px; height: 198px; }
  .photo-seed { background: linear-gradient(135deg, #e2e3e4 0%, #b7c0cb 100%); }
  .photo-sunset { background: linear-gradient(180deg, #3b2e3e 0%, #7a4a4a 25%, #c6a277 48%, #3f8b8a 62%, #2b5c5a 100%); }
  .photo-wheat { background: linear-gradient(180deg, #cfe3f3 0%, #d8c49a 50%, #b57b2c 100%); }
  .bottom-btn { position: absolute; left: 429px; top: 1084px; width: 141px; height: 35px; line-height: 35px; }
  .footer-band {
    position: absolute; left: 0; top: 1144px; width: 1000px; height: 56px;
    background: linear-gradient(160deg, var(--sand-light), var(--sand-dark));
    border-top: 2px solid #bfb39f; box-shadow: inset 0 2px 2px rgba(0,0,0,0.08);
  }
  .footer-nav a { position: absolute; top: 17px; white-space: nowrap; }
  .copyright { position: absolute; right: 107px; top: 17px; font-size: 12.5px; color: var(--text); }
</style>
</head>
<body>
  <header class="header-band">
    <div class="brand">
      <div class="brand-mark"></div>
      <span class="brand-name">The Steady Harbor</span>
    </div>
    <nav class="main-nav">
      <a class="current" href="#" style="left:0">Home</a>
      <a href="#" style="left:71px">About</a>
      <a href="#" style="left:145px">Services</a>
      <a href="#" style="left:230px">Events</a>
      <a href="#" style="left:303px">Contact</a>
      <a href="#" style="left:385px">Find Us</a>
    </nav>
    <div class="hero-frame">
      <div class="hero-image" role="img" aria-label="Bright tropical beach with sun, turquoise waves and palm leaves"></div>
      <div class="hero-panel">
        <h1 class="hero-title"><span class="hl">Life coaching</span> and<br><span class="hl">change consultation</span><br>for professionals</h1>
        <p class="hero-text">Morbi quis augue venenatis, auctor orci utmo llis ipsum proin augue nisl, tempor id velit sit</p>
        <a class="btn" href="#">Contact Us</a>
      </div>
    </div>
  </header>
  <div class="accent-rule"></div>

  <h2 class="section-title" style="top:425px">What we do &amp; how we can help you...</h2>
  <div class="section-rule" style="top:455px"></div>
  <div class="intro">
    <p>Lorem ipsum dolor sit amet, consectetur adipiscing elit. In aliquet malesuada ultrices. Vivamus varius, nisl et placerat rhoncus, augue nisi lobortis nunc, sit amet sagittis tortor sem eu tellus. Cum sociis natoque penatibus et magnis dis parturient montes, nascetur ridiculus mus.</p>
    <p>Dum sociis natoque penatibus et magnis dis parturient montes, nascetur ridiculus musullam at leo leom Integer vitae imperdiet nunc. Nulla lacus nulla, ultrices quis sem ut. <a class="more" href="#">Contact Us &gt;</a></p>
  </div>

  <h2 class="section-title" style="top:634px">List of features &amp; services...</h2>
  <div class="section-rule" style="top:664px"></div>

  <ul class="feature-list" style="left:126px">
    <li><svg width="6" height="9" viewBox="0 0 6 9"><path d="M1 1l3.5 3.5L1 8" stroke="#8fbf2f" stroke-width="2" fill="none"/></svg>Lorem ipsum dolor sit amet</li>
    <li><svg width="6" height="9" viewBox="0 0 6 9"><path d="M1 1l3.5 3.5L1 8" stroke="#8fbf2f" stroke-width="2" fill="none"/></svg>Sectetur adipiscing elitn aliquet</li>
    <li><svg width="6" height="9" viewBox="0 0 6 9"><path d="M1 1l3.5 3.5L1 8" stroke="#8fbf2f" stroke-width="2" fill="none"/></svg>Vivamus varius nisl et placerat</li>
    <li><svg width="6" height="9" viewBox="0 0 6 9"><path d="M1 1l3.5 3.5L1 8" stroke="#8fbf2f" stroke-width="2" fill="none"/></svg>Im sociis natoque penatibus</li>
  </ul>
  <ul class="feature-list" style="left:403px">
    <li><svg width="6" height="9" viewBox="0 0 6 9"><path d="M1 1l3.5 3.5L1 8" stroke="#8fbf2f" stroke-width="2" fill="none"/></svg>Donec ut molestie elit.</li>
    <li><svg width="6" height="9" viewBox="0 0 6 9"><path d="M1 1l3.5 3.5L1 8" stroke="#8fbf2f" stroke-width="2" fill="none"/></svg>Duis in dictum ligula id volutpat</li>
    <li><svg width="6" height="9" viewBox="0 0 6 9"><path d="M1 1l3.5 3.5L1 8" stroke="#8fbf2f" stroke-width="2" fill="none"/></svg>Aliquam erat volutpat.</li>
    <li><svg width="6" height="9" viewBox="0 0 6 9"><path d="M1 1l3.5 3.5L1 8" stroke="#8fbf2f" stroke-width="2" fill="none"/></svg>Curabitur vestibulum luctus mal</li>
  </ul>
  <ul class="feature-list" style="left:675px">
    <li><svg width="6" height="9" viewBox="0 0 6 9"><path d="M1 1l3.5 3.5L1 8" stroke="#8fbf2f" stroke-width="2" fill="none"/></svg>Lorem ipsum dolor sit amet</li>
    <li><svg width="6" height="9" viewBox="0 0 6 9"><path d="M1 1l3.5 3.5L1 8" stroke="#8fbf2f" stroke-width="2" fill="none"/></svg>Sectetur adipiscing elitn aliquet</li>
    <li><svg width="6" height="9" viewBox="0 0 6 9"><path d="M1 1l3.5 3.5L1 8" stroke="#8fbf2f" stroke-width="2" fill="none"/></svg>Vivamus varius nisl et placerat</li>
    <li><svg width="6" height="9" viewBox="0 0 6 9"><path d="M1 1l3.5 3.5L1 8" stroke="#8fbf2f" stroke-width="2" fill="none"/></svg>Im sociis natoque penatibus</li>
  </ul>

  <div class="gallery-card" style="left:104px"><div class="photo photo-seed" role="img" aria-label="Dandelion seeds drifting against a pale sky"></div></div>
  <div class="gallery-card" style="left:375px"><div class="photo photo-sunset" role="img" aria-label="Sunset over a calm sea with rocks in the shallows"></div></div>
  <div class="gallery-card" style="left:646px"><div class="photo photo-wheat" role="img" aria-label="Golden wheat ears against a bright sky"></div></div>

  <a class="btn bottom-btn" href="#">Contact Us</a>

  <footer class="footer-band">
    <nav class="footer-nav">
      <a class="current" href="#" style="left:105px">Home</a>
      <a href="#" style="left:176px">About</a>
      <a href="#" style="left:250px">Services</a>
      <a href="#" style="left:335px">Events</a>
      <a href="#" style="left:409px">Contact</a>
      <a href="#" style="left:490px">Find Us</a>
    </nav>
    <p class="copyright">© 2013 Company Name</p>
  </footer>
</body>
</html>
```